Business card for Quorvane, LLC

I need a business card template in .ai or similar format for my IT consultancy, Quorvane(.com)

Front side: The usual name/title/number/fax/email/contact info. Definitely san-serif, the logo font is MuseoSans 500 so the company name (Quorvane, LLC.) should definitely be in the same type and the rest of the text should be that or something complimentary. Including logo on the front is optional - I would prefer designs that include both with and without. I am open to creative input on the format.

Back side: Company logo framed somehow. I was thinking red background with the logo in a white circle in the middle, tho' I'm not sure how that would play off the red ball in the elephant's trunk. Open to creative input here too.

Attached are a (very rough) one-sided card mock-up I made, along with the logo and logo font.

```html
<!DOCTYPE html>
<html lang="en">
<head>
<meta charset="utf-8">
<title>Quorvane, LLC — Business Card</title>
<link rel="stylesheet" href="https://fonts.googleapis.com/css2?family=Archivo+Narrow:wght@400&family=Arimo:wght@400&display=swap">
<style>
  :root {
    --frame-red: #c8102e;
    --brand-red: #d90a12;
    --page: #ffffff;
    --panel: #f6f6f6;
    --divider: #e2e2e2;
    --ink: #1e1e1e;
    --muted: #7a7a7a;
  }
  html, body {
    margin: 0;
    padding: 0;
    width: 1200px;
    height: 741px;
    overflow: hidden;
    background: var(--page);
  }
  .card {
    position: relative;
    width: 1200px;
    height: 741px;
    background: var(--page);
    font-family: "Arimo", Arial, sans-serif;
    color: var(--ink);
  }
  .card-frame {
    position: absolute;
    left: 17px;
    top: 17px;
    width: 1166px;
    height: 704px;
    box-sizing: border-box;
    border: 3.5px solid var(--frame-red);
  }
  .card-panel {
    position: absolute;
    left: 41px;
    top: 41px;
    width: 1120px;
    height: 659px;
    background: var(--panel);
  }
  .divider {
    position: absolute;
    left: 602px;
    top: 146px;
    width: 1px;
    height: 448px;
    background: var(--divider);
  }
  .brand {
    position: absolute;
    left: 170px;
    width: 400px;
    top: 300px;
    display: flex;
    align-items: center;
    justify-content: center;
    gap: 16px;
  }
  .brand-dot {
    width: 22px;
    height: 22px;
    border-radius: 50%;
    background: var(--brand-red);
    flex: none;
  }
  .brand-name {
    margin: 0;
    font-family: "Arimo", Arial, sans-serif;
    font-weight: 400;
    font-size: 50px;
    line-height: 1;
    color: var(--ink);
  }
  .person-name {
    position: absolute;
    left: 634px;
    top: 259px;
    margin: 0;
    font-family: "Archivo Narrow", "Arial Narrow", sans-serif;
    font-weight: 400;
    font-size: 37px;
    line-height: 1;
    color: var(--ink);
  }
  .person-title {
    position: absolute;
    left: 635px;
    top: 301px;
    margin: 0;
    font-size: 13.5px;
    letter-spacing: 0.6px;
    word-spacing: 3px;
    line-height: 1;
  }
  .address {
    position: absolute;
    left: 638px;
    top: 363px;
    margin: 0;
    font-style: normal;
    font-size: 15px;
    line-height: 17.5px;
    letter-spacing: 0.6px;
  }
  .contact {
    position: absolute;
    left: 637px;
    top: 410px;
    margin: 0;
    font-size: 15.5px;
    line-height: 24.5px;
  }
  .contact-row { white-space: nowrap; }
  .contact-label {
    display: inline-block;
    width: 54px;
    letter-spacing: 0.4px;
  }
  .contact-sep { display: inline-block; width: 13px; }
  .contact-label-inline {
    display: inline-block;
    margin-left: 12px;
    width: 45px;
    letter-spacing: 0.4px;
  }
  .website {
    position: absolute;
    left: 0;
    width: 1240px;
    top: 676px;
    margin: 0;
    text-align: center;
    font-size: 11.5px;
    letter-spacing: 4.2px;
    color: var(--muted);
    line-height: 1;
  }
</style>
</head>
<body>
  <div class="card">
    <div class="card-frame"></div>
    <div class="card-panel"></div>
    <div class="divider"></div>

    <div class="brand">
      <span class="brand-dot" aria-hidden="true"></span>
      <p class="brand-name">Quorvane</p>
    </div>

    <h1 class="person-name">Dalen Morrow</h1>
    <p class="person-title">Problem Eliminator</p>

    <address class="address">27 Fernbrook Rd.<br>Oak Vale, PA 19320 - 4418</address>

    <div class="contact">
      <div class="contact-row"><span class="contact-label">Tel</span><span class="contact-sep">:</span>1.800.555.0147<span class="contact-label-inline">Mob</span><span class="contact-sep">:</span>1.215.555.0182</div>
      <div class="contact-row"><span class="contact-label">Fax</span><span class="contact-sep">:</span>1.215.555.0136</div>
      <div class="contact-row"><span class="contact-label">Email</span><span class="contact-sep">:</span>dmorrow@quorvane.com</div>
    </div>

    <p class="website">www.quorvane.com</p>
  </div>
</body>
</html>
```